Flyer Design Project

We want to design a flyer for a laundromat in San Francisco. It will be used to market the services of the laundromat. I am uploading a .jpg file with details to be highlighted. The flyer should be of size 8.5 in x 11 in and should be attractive and hard hitting. The attachment should only be used for the copy, not for design.

Target Market(s)

Laundromat and laundry users

Requirements
Must have
• Must have a attention grabbing headline
Nice to have
• Pictures

```html
<!DOCTYPE html>
<html lang="en">
<head>
<meta charset="utf-8">
<title>Juniper Laundromat Flyer</title>
<link rel="stylesheet" href="https://fonts.googleapis.com/css2?family=Roboto+Condensed:wght@700&family=Rubik:wght@800&display=swap">
<style>
  :root {
    --backdrop: #e9e4dc;
    --paper: #ffffff;
    --swoosh-blue: #3a7ee8;
    --swoosh-green: #8ef00f;
    --panel-blue: #0a31c9;
    --brand-green: #a6e61a;
    --brand-blue: #1d3fbf;
    --ink: #1c1c1c;
    --scribble: #333536;
    --rule: #111111;
  }
  * { margin: 0; padding: 0; box-sizing: border-box; }
  html, body { width: 1200px; height: 951px; overflow: hidden; background: var(--backdrop); }
  .flyer {
    position: absolute; left: 14px; top: 20px; width: 1176px; height: 915px;
    background: var(--paper); overflow: hidden;
    box-shadow: 0 4px 14px rgba(0,0,0,.35);
  }
  .swoosh { position: absolute; left: -14px; top: -20px; width: 1200px; height: 951px; }
  .fold-rule { position: absolute; left: 587px; top: 12px; width: 2px; height: 570px; background: var(--rule); }
  .corner-scribble { position: absolute; right: 0; top: 0; width: 510px; height: 160px; }
  .brand-small {
    position: absolute; left: 265px; top: 14px; display: flex; align-items: center; gap: 10px;
    font-family: "Roboto Condensed", sans-serif; font-weight: 700; color: var(--brand-blue);
    font-size: 21px; line-height: 0.95;
  }
  .brand-small .mark { width: 40px; height: 40px; border-radius: 50%; background: #cfd6dc; border: 3px solid #9aa3aa; }
  .photo {
    position: absolute; left: 158px; top: 190px; width: 351px; height: 267px;
    background: linear-gradient(160deg, #f2f4f6 0%, #c9ced4 45%, #7d8796 70%, #e3c44a 100%);
  }
  .tagline {
    position: absolute; left: 288px; top: 466px;
    font-family: "Rubik", sans-serif; font-weight: 800; font-size: 37px; color: var(--ink); letter-spacing: 0.5px;
  }
  .brand-panel {
    position: absolute; left: 589px; top: 155px; width: 577px; height: 343px; background: var(--panel-blue);
    display: flex; align-items: center; gap: 30px; padding-left: 72px;
  }
  .brand-panel .mark { width: 142px; height: 142px; border-radius: 50%; background: #c7ced6; border: 8px solid #8f98a1; flex: none; }
  .brand-panel .name {
    font-family: "Roboto Condensed", sans-serif; font-weight: 700; color: var(--brand-green);
    font-size: 64px; line-height: 1.15;
  }
  .contact {
    position: absolute; left: 13px; top: 815px;
    font-family: "Roboto Condensed", sans-serif; font-weight: 700; font-size: 17px; line-height: 1.45; color: var(--ink);
  }
</style>
</head>
<body>
<div class="flyer">
  <svg class="swoosh" viewBox="0 0 1200 951" aria-hidden="true">
    <path fill="var(--swoosh-blue)" d="M270,35 C120,150 20,330 40,520 C60,720 250,900 600,920 C850,930 1050,860 1180,760 L1180,610 C950,650 700,660 500,640 C300,620 170,520 150,380 C135,250 190,130 270,35 Z"/>
    <path fill="var(--swoosh-green)" d="M270,35 C190,130 135,250 150,380 C170,520 300,620 500,640 C700,660 950,650 1180,610 L1180,555 C950,600 700,620 520,585 C340,555 220,470 200,350 C185,230 215,130 270,35 Z"/>
  </svg>

  <svg class="corner-scribble" viewBox="0 0 510 160" role="img" aria-label="Dark hand-drawn scribble in the top corner">
    <path fill="var(--scribble)" d="M0,8 L510,0 L510,160 C440,110 320,40 0,8 Z"/>
  </svg>

  <div class="fold-rule"></div>

  <div class="brand-small">
    <span class="mark"></span>
    <span>Juniper<br>laundromat</span>
  </div>

  <div class="photo" role="img" aria-label="Photo of a laundromat with rows of washers and two people in blue and yellow suits playfully wrestling"></div>

  <div class="tagline">...laundry time</div>

  <div class="brand-panel">
    <span class="mark"></span>
    <span class="name">Juniper<br>laundromat</span>
  </div>

  <div class="contact">
    Juniper Laundromat<br>
    Tel #: 415 555 0142<br>
    2218 C Marlow Street&nbsp;&nbsp; San Francisco CA 94117
  </div>
</div>
</body>
</html>
```